New Business Cards for Torvin Group

We need a new Business Card to compliment our new logo. We are a vibrant design, manufacture and install business providing recreation areas, public parks and Municipal spaces. We want business cards that are classy, modern and clean.

We have recently changed our logo, and are celebrating our 40th anniversary. We want business cards with a new modern design to reflect our status.

Target Market(s)

Customers

Contact Information for Business Card

We need all the details of our 3 offices as per the business card attached. Please disregard the old logo on the business card, the other three files show our new logo.

Requirements
Must have
• All info as per attached business card but with new logo.
Nice to have

```html
<!DOCTYPE html>
<html lang="en">
<head>
<meta charset="utf-8">
<title>Torvin Group – Business Card</title>
<link href="https://fonts.googleapis.com/css2?family=Michroma&family=Open+Sans:wght@400;600;700&display=swap" rel="stylesheet">
<style>
  :root {
    --bg: #e6e3df;
    --card: #f8f6f2;
    --ink: #1b1b1b;
    --brand-ink: #4a4a4d;
    --rule: #77777a;
    --red: #e4203a;
    --red-orange: #e85a1f;
    --orange: #f0891b;
    --white: #ffffff;
  }
  * { margin: 0; padding: 0; box-sizing: border-box; }
  html, body { width: 1200px; height: 800px; overflow: hidden; background: var(--bg); }
  body { font-family: "Open Sans", sans-serif; color: var(--ink); position: relative; }

  .card {
    position: absolute; left: 100px; top: 110px;
    width: 1000px; height: 580px;
    background: var(--card);
    box-shadow: 0 12px 30px rgba(0,0,0,.18);
    overflow: hidden;
  }
  .card-graphics { position: absolute; inset: 0; }

  .brand { position: absolute; left: 80px; top: 180px; display: flex; align-items: center; gap: 16px; }
  .brand-dot { width: 84px; height: 84px; border-radius: 50%; background: var(--red); flex: none; }
  .brand-name { font-weight: 700; font-size: 38px; letter-spacing: 1px; color: var(--brand-ink); line-height: 1.05; }

  .person { position: absolute; left: 96px; top: 300px; }
  .person-name { font-weight: 700; font-size: 50px; line-height: 1; }
  .person-role { font-size: 25px; margin-top: 6px; }
  .person-contact { position: absolute; left: 96px; top: 398px; font-size: 25px; line-height: 1.3; }

  .office { position: absolute; font-size: 13px; line-height: 1.35; white-space: nowrap; }
  .office-title { font-family: "Michroma", sans-serif; font-size: 18px; letter-spacing: 2px; text-transform: uppercase; margin-bottom: 2px; }
  .office--head { left: 450px; top: 70px; }
  .office--qatar { left: 725px; top: 10px; transform-origin: left top; transform: translate(0, 235px) rotate(-90deg); }
  .office--dubai { left: 780px; top: 318px; }

  .website {
    position: absolute; left: 330px; top: 528px;
    font-family: "Michroma", sans-serif; font-size: 15px; letter-spacing: 2.5px;
    color: var(--white); text-transform: uppercase;
  }
</style>
</head>
<body>
  <div class="card">
    <svg class="card-graphics" width="1000" height="580" viewBox="0 0 1000 580" aria-hidden="true">
      <rect class="band band--red" x="0" y="470" width="1000" height="110" fill="var(--red)"/>
      <polygon class="band band--mid" points="577,470 1000,470 1000,580 640,580" fill="var(--red-orange)"/>
      <polygon class="band band--orange" points="743,440 1000,440 1000,580 730,580" fill="var(--orange)"/>
      <line class="rule rule--main" x1="335" y1="0" x2="655" y2="580" stroke="var(--rule)" stroke-width="6"/>
      <line class="rule rule--dubai" x1="765" y1="305" x2="735" y2="580" stroke="var(--rule)" stroke-width="6"/>
      <line class="rule rule--qatar" x1="700" y1="250" x2="1000" y2="298" stroke="var(--rule)" stroke-width="6"/>
    </svg>

    <div class="brand">
      <span class="brand-dot"></span>
      <span class="brand-name">TORVIN<br>GROUP</span>
    </div>

    <div class="person">
      <div class="person-name">Marek Delvani</div>
      <div class="person-role">Managing Partner</div>
    </div>
    <div class="person-contact">
      <div>Mobile no : + 971 050 4837 126</div>
      <div>Email: marek@torvingroup.com</div>
    </div>

    <div class="office office--head">
      <div class="office-title">Head Office</div>
      <div>P.O. Box : 48213 Abu Dhabi , U.A.E.</div>
      <div>Tel No: +971(0)2 5518302</div>
      <div>Fax No: + 971(0)2 5518303</div>
      <div>Email: sales@torvingroup.com</div>
    </div>

    <div class="office office--qatar">
      <div class="office-title">Qatar Office</div>
      <div>P.O. Box : 30972 Doha , Qatar.</div>
      <div>Tel No: +971(0)2 5518302</div>
      <div>Fax No: + 971(0)2 5518303</div>
      <div>Email: sales@torvingroup.com</div>
    </div>

    <div class="office office--dubai">
      <div class="office-title">Dubai Office</div>
      <div>P.O. Box : 571084 Dubai ,U.A.E.</div>
      <div>Tel No: +971(0)4 6227140</div>
      <div>Fax No: + 971(0)4 6227141</div>
      <div>Email: sales@torvingroup.com</div>
    </div>

    <div class="website">www.torvingroup.com</div>
  </div>
</body>
</html>
```